Brenton Wealth Management Flow Charts

I need help creating three flow charts for my businesses website. We want them to be simple but look professional. This is for a Wealth Management firm. I will attach a word document that has all of the descriptions for everything so you know what icons to use. We just want the chart to have an icon, the names of each step and the corresponding numbers. I will also include some examples of charts we liked as well. Once the winner is selected, we will need help with additional graphic design elements for our website ASAP.
- Goudy Roman

```html
<!DOCTYPE html>
<html lang="en">
<head>
<meta charset="utf-8">
<title>Brenton Wealth Management – Flow Charts</title>
<link href="https://fonts.googleapis.com/css2?family=Oswald:wght@400;500;600&family=Roboto+Condensed:wght@400;700&family=Roboto:wght@400&display=swap" rel="stylesheet">
<style>
  :root{
    --backdrop:#807f84;
    --panel:#ffffff;
    --blue-deep:#1a56a6;
    --blue-mid:#3f6db4;
    --blue-soft:#7f9bcc;
    --grey-light:#a7a9ac;
    --grey-mid:#7d7e81;
    --grey-dark:#636466;
    --grey-pale:#efefef;
    --ink:#4a4a4c;
    --line:#58595b;
  }
  html,body{margin:0;padding:0;overflow:hidden;background:var(--backdrop);}
  .canvas{width:1200px;height:853px;display:block;}
  .heading{font-family:"Oswald",sans-serif;font-weight:600;}
  .heading-blue{fill:var(--blue-deep);}
  .heading-ink{fill:var(--ink);}
  .wedge-label{font-family:"Roboto Condensed",sans-serif;font-weight:700;font-size:9.5px;fill:#fff;}
  .step-number{font-family:"Oswald",sans-serif;font-weight:500;font-size:17px;}
  .step-text{font-family:"Roboto",sans-serif;font-size:9.5px;fill:#333;}
  .brand{font-family:"Oswald",sans-serif;font-weight:400;fill:var(--ink);}
  .milestone-label{font-family:"Roboto Condensed",sans-serif;font-weight:700;font-size:9px;fill:#fff;}
  .big-digit{font-family:"Oswald",sans-serif;font-weight:500;font-size:92px;fill:#fff;stroke:#6d6e71;stroke-width:2.5;}
  .icon{fill:none;stroke:var(--blue-deep);stroke-width:1.6;stroke-linecap:round;stroke-linejoin:round;}
  .icon-light{fill:none;stroke:#fff;stroke-width:2;stroke-linecap:round;stroke-linejoin:round;}
  .leader{stroke:var(--blue-mid);stroke-width:1;stroke-dasharray:2 2;}
</style>
</head>
<body>
<svg class="canvas" viewBox="0 0 1561 1110" xmlns="http://www.w3.org/2000/svg">
  <defs>
    <filter id="soft-shadow" x="-30%" y="-30%" width="160%" height="160%">
      <feDropShadow dx="0" dy="2" stdDeviation="3" flood-color="#000" flood-opacity="0.28"/>
    </filter>
    <filter id="panel-shadow" x="-5%" y="-5%" width="110%" height="115%">
      <feDropShadow dx="0" dy="6" stdDeviation="6" flood-color="#000" flood-opacity="0.25"/>
    </filter>
    <marker id="arrow-head" viewBox="0 0 10 10" refX="5" refY="5" markerWidth="5" markerHeight="5" orient="auto">
      <path d="M0 0 L10 5 L0 10 Z" fill="var(--blue-deep)"/>
    </marker>
    <marker id="timeline-head" viewBox="0 0 10 10" refX="5" refY="5" markerWidth="6" markerHeight="6" orient="auto">
      <path d="M0 0 L10 5 L0 10 Z" fill="var(--line)"/>
    </marker>
  </defs>

  <!-- Panels -->
  <rect x="74" y="48" width="700" height="490" fill="var(--panel)" filter="url(#panel-shadow)"/>
  <rect x="800" y="48" width="701" height="490" fill="var(--panel)" filter="url(#panel-shadow)"/>
  <rect x="368" y="560" width="832" height="490" fill="var(--panel)" filter="url(#panel-shadow)"/>

  <!-- Retirement planning process -->
  <g class="retirement-cycle">
    <path d="M348.8 135.7 A178 178 0 1 0 499.2 135.7" fill="none" stroke="var(--blue-deep)" stroke-width="2" marker-end="url(#arrow-head)"/>
    <text class="heading heading-blue" x="424" y="144" font-size="15" text-anchor="middle">THE RETIREMENT</text>
    <line x1="400" y1="153" x2="448" y2="153" stroke="var(--blue-deep)" stroke-width="1.5"/>
    <text class="heading heading-ink" x="424" y="172" font-size="12" text-anchor="middle">PLANNING</text>
    <text class="heading heading-ink" x="424" y="185" font-size="12" text-anchor="middle">PROCESS</text>
    <g fill="none" stroke="var(--blue-mid)" stroke-width="1.4">
      <circle cx="413" cy="198" r="2.6"/><circle cx="424" cy="198" r="2.6"/><circle cx="435" cy="198" r="2.6"/>
    </g>

    <path d="M424 297 L483.2 170.1 A140 140 0 0 1 561.4 270.3 Z" fill="var(--blue-deep)"/>
    <path d="M424 297 L561.4 270.3 A140 140 0 0 1 535.8 381.3 Z" fill="var(--blue-mid)"/>
    <path d="M424 297 L535.8 381.3 A140 140 0 0 1 424 437 Z" fill="var(--blue-soft)"/>
    <path d="M424 297 L424 437 A140 140 0 0 1 309.3 377.3 Z" fill="var(--grey-dark)"/>
    <path d="M424 297 L309.3 377.3 A140 140 0 0 1 292.4 249.1 Z" fill="var(--grey-mid)"/>
    <path d="M424 297 L292.4 249.1 A140 140 0 0 1 367.1 169.1 Z" fill="var(--grey-light)"/>

    <text class="wedge-label" x="353" y="237" text-anchor="middle">DISCOVERY</text>
    <text class="wedge-label" x="353" y="248" text-anchor="middle">MEETING</text>
    <text class="wedge-label" x="496" y="239" text-anchor="middle">REVIEW</text>
    <text class="wedge-label" x="509" y="322" text-anchor="middle">ALIGNMENT</text>
    <text class="wedge-label" x="469" y="380" text-anchor="middle">EXECUTION</text>
    <text class="wedge-label" x="378" y="380" text-anchor="middle">PLANNING</text>
    <text class="wedge-label" x="340" y="320" text-anchor="middle">LEARNING</text>

    <circle cx="424" cy="297" r="60" fill="#fff" filter="url(#soft-shadow)"/>
    <text class="brand" x="424" y="297" font-size="20" text-anchor="middle">BRENTON</text>
    <text class="brand" x="424" y="312" font-size="7" text-anchor="middle" letter-spacing="0.5">WEALTH MANAGEMENT</text>

    <g filter="url(#soft-shadow)" fill="#fff">
      <circle cx="313" cy="202" r="26"/><circle cx="533" cy="202" r="26"/>
      <circle cx="565" cy="320" r="26"/><circle cx="482" cy="412" r="26"/>
      <circle cx="364" cy="412" r="26"/><circle cx="286" cy="318" r="26"/>
    </g>
    <g fill="none" stroke="#cfd0d2" stroke-width="1">
      <circle cx="313" cy="202" r="21"/><circle cx="533" cy="202" r="21"/>
      <circle cx="565" cy="320" r="21"/><circle cx="482" cy="412" r="21"/>
      <circle cx="364" cy="412" r="21"/><circle cx="286" cy="318" r="21"/>
    </g>
    <g class="icon" stroke="var(--grey-dark)">
      <circle cx="306" cy="198" r="3"/><circle cx="320" cy="198" r="3"/><circle cx="313" cy="195" r="3"/>
      <path d="M301 210 q5 -8 12 -8 q7 0 12 8"/>
      <path d="M276 310 h10 v16 h-10 z M286 310 h10 v16 h-10 z"/>
      <rect x="356" y="402" width="16" height="20" rx="1"/><path d="M359 409 l2 2 l3 -3 M359 416 l2 2 l3 -3 M366 416 l6 -8"/>
    </g>
    <g class="icon">
      <path d="M522 206 h6 l8 -6 v12 h-14 z"/><rect x="538" y="193" width="5" height="18"/>
      <path d="M565 306 v10 M561 312 l4 4 l4 -4 M557 320 h16 M565 334 v-10 M561 328 l4 -4 l4 4"/>
      <path d="M482 398 q7 8 3 20 h-6 q-4 -12 3 -20 z M479 418 l-3 6 M485 418 l3 6"/>
    </g>
  </g>

  <!-- Comprehensive investment management -->
  <g class="investment-wheel">
    <text class="heading" x="1152" y="124" font-size="21" text-anchor="middle"><tspan class="heading-blue">COMPREHENSIVE</tspan><tspan class="heading-ink"> INVESTMENT MANAGEMENT</tspan></text>

    <path d="M1155 197 A153 153 0 0 0 1155 503 Z" fill="var(--grey-pale)"/>
    <path d="M1155 197 A153 153 0 0 1 1284.7 268.0 L1235.6 300.2 A95 95 0 0 0 1155 255 Z" fill="var(--blue-deep)"/>
    <path d="M1284.7 268.0 A153 153 0 0 1 1288.7 423.0 L1243.4 394.6 A95 95 0 0 0 1235.6 300.2 Z" fill="var(--blue-mid)"/>
    <path d="M1288.7 423.0 A153 153 0 0 1 1155 503 L1155 445 A95 95 0 0 0 1243.4 394.6 Z" fill="var(--blue-soft)"/>

    <path d="M1155 240 A110 110 0 0 0 1059.7 295 L1103 320 A60 60 0 0 1 1155 290 Z" fill="var(--grey-light)"/>
    <path d="M1059.7 295 A110 110 0 0 0 1059.7 405 L1103 380 A60 60 0 0 1 1103 320 Z" fill="var(--grey-mid)"/>
    <path d="M1059.7 405 A110 110 0 0 0 1155 460 L1155 410 A60 60 0 0 1 1103 380 Z" fill="var(--grey-dark)"/>

    <circle cx="1155" cy="350" r="58" fill="#fff" filter="url(#soft-shadow)"/>
    <text class="brand" x="1155" y="352" font-size="19" text-anchor="middle">BRENTON</text>
    <text class="brand" x="1155" y="366" font-size="6.5" text-anchor="middle" letter-spacing="0.5">WEALTH MANAGEMENT</text>

    <g class="icon-light">
      <path d="M1096 288 a17 17 0 0 1 34 0 M1113 288 l6 -8"/>
      <circle cx="1073" cy="349" r="11"/><circle cx="1073" cy="349" r="5"/><path d="M1073 349 l12 -10"/>
      <circle cx="1110" cy="417" r="11"/><path d="M1110 410 v14 M1114 413 h-6 q-3 4 2 4 q5 0 1 4 h-5"/>
      <circle cx="1222" cy="234" r="10"/><path d="M1222 229 v6 M1222 238 v1"/>
      <circle cx="1285" cy="349" r="6"/><path d="M1285 343 v-8 M1279 352 l-7 5 M1291 352 l7 5"/>
      <circle cx="1219" cy="461" r="11"/><path d="M1214 466 l10 -10 M1215 457 h1 M1223 465 h1"/>
    </g>

    <text class="step-number" x="908" y="235" fill="var(--grey-mid)">1</text>
    <text class="step-text" x="908" y="251">Understanding your Risk Tolerance</text>
    <line class="leader" x1="908" y1="259" x2="1092" y2="259"/>
    <text class="step-number" x="908" y="320" fill="var(--grey-mid)">2</text>
    <text class="step-text" x="908" y="338">Investment Selection</text>
    <line class="leader" x1="908" y1="347" x2="1048" y2="347"/>
    <text class="step-number" x="908" y="412" fill="var(--grey-mid)">3</text>
    <text class="step-text" x="908" y="427">Asset Allocation</text>
    <line class="leader" x1="908" y1="436" x2="1090" y2="436"/>

    <text class="step-number" x="1400" y="195" text-anchor="end" fill="var(--blue-deep)">6</text>
    <text class="step-text" x="1402" y="212" text-anchor="end">Behavior Finance Coaching</text>
    <line class="leader" x1="1245" y1="221" x2="1402" y2="221"/>
    <text class="step-number" x="1400" y="326" text-anchor="end" fill="var(--blue-mid)">5</text>
    <text class="step-text" x="1402" y="340" text-anchor="end">Distribution Strategy</text>
    <line class="leader" x1="1300" y1="348" x2="1402" y2="348"/>
    <text class="step-number" x="1400" y="453" text-anchor="end" fill="var(--blue-soft)">4</text>
    <text class="step-text" x="1402" y="467" text-anchor="end">Tax efficiency</text>
    <line class="leader" x1="1245" y1="476" x2="1402" y2="476"/>
  </g>

  <!-- Legacy and estate planning -->
  <g class="legacy-timeline">
    <text class="brand" x="795" y="665" font-size="22" text-anchor="middle">BRENTON</text>
    <text class="brand" x="795" y="677" font-size="6.5" text-anchor="middle" letter-spacing="0.5">WEALTH MANAGEMENT</text>
    <text class="heading" x="795" y="710" font-size="20" text-anchor="middle"><tspan class="heading-blue">LEGACY AND ESTATE</tspan><tspan class="heading-ink"> PLANNING</tspan></text>

    <line x1="465" y1="901" x2="1104" y2="901" stroke="var(--line)" stroke-width="1.5" marker-end="url(#timeline-head)"/>

    <g class="milestone">
      <text class="big-digit" x="455" y="846">1</text>
      <line x1="528" y1="865" x2="528" y2="901" stroke="var(--line)" stroke-width="1.5"/><circle cx="528" cy="901" r="3.5" fill="var(--line)"/>
      <circle cx="528" cy="815" r="50" fill="#fff" stroke="#8d8e91" stroke-width="2"/>
      <circle cx="528" cy="815" r="42" fill="#fff" filter="url(#soft-shadow)"/>
      <path d="M486 815 A42 42 0 0 0 570 815 Z" fill="var(--blue-deep)"/>
      <text class="milestone-label" x="528" y="835" text-anchor="middle">BENEFICIARIES</text>
      <g class="icon"><circle cx="524" cy="790" r="5"/><path d="M516 806 q8 -10 16 0 M540 784 v16 M543 787 h-5 q-3 4 2 4 q5 0 1 4 h-5"/></g>
    </g>
    <g class="milestone">
      <text class="big-digit" x="588" y="846">2</text>
      <line x1="661" y1="865" x2="661" y2="901" stroke="var(--line)" stroke-width="1.5"/><circle cx="661" cy="901" r="3.5" fill="var(--line)"/>
      <circle cx="661" cy="815" r="50" fill="#fff" stroke="#8d8e91" stroke-width="2"/>
      <circle cx="661" cy="815" r="42" fill="#fff" filter="url(#soft-shadow)"/>
      <path d="M619 815 A42 42 0 0 0 703 815 Z" fill="var(--blue-deep)"/>
      <text class="milestone-label" x="661" y="836" text-anchor="middle">TRUSTS</text>
      <g class="icon"><path d="M642 792 h5 v14 h-5 M680 792 h-5 v14 h5 M647 796 l8 -3 l6 3 l8 -3 l6 3 M651 801 l6 5 l6 0 l6 -5"/></g>
    </g>
    <g class="milestone">
      <text class="big-digit" x="722" y="846">3</text>
      <line x1="795" y1="865" x2="795" y2="901" stroke="var(--line)" stroke-width="1.5"/><circle cx="795" cy="901" r="3.5" fill="var(--line)"/>
      <circle cx="795" cy="815" r="50" fill="#fff" stroke="#8d8e91" stroke-width="2"/>
      <circle cx="795" cy="815" r="42" fill="#fff" filter="url(#soft-shadow)"/>
      <path d="M753 815 A42 42 0 0 0 837 815 Z" fill="var(--blue-deep)"/>
      <text class="milestone-label" x="795" y="828" text-anchor="middle">ESTATE TAXES</text>
      <text class="milestone-label" x="795" y="838" text-anchor="middle">AND ASSESSMENT</text>
      <g class="icon"><rect x="780" y="786" width="32" height="22"/><path d="M780 791 h32"/><circle cx="797" cy="800" r="5"/><path d="M801 804 l5 4"/></g>
    </g>
    <g class="milestone">
      <text class="big-digit" x="855" y="846">4</text>
      <line x1="928" y1="865" x2="928" y2="901" stroke="var(--line)" stroke-width="1.5"/><circle cx="928" cy="901" r="3.5" fill="var(--line)"/>
      <circle cx="928" cy="815" r="50" fill="#fff" stroke="#8d8e91" stroke-width="2"/>
      <circle cx="928" cy="815" r="42" fill="#fff" filter="url(#soft-shadow)"/>
      <path d="M886 815 A42 42 0 0 0 970 815 Z" fill="var(--blue-deep)"/>
      <text class="milestone-label" x="928" y="834" text-anchor="middle">ANNUAL GIVING</text>
      <g class="icon"><rect x="913" y="786" width="22" height="20"/><path d="M913 791 h22 M918 783 v5 M930 783 v5"/><rect x="926" y="797" width="16" height="12" fill="#fff"/></g>
    </g>
    <g class="milestone">
      <text class="big-digit" x="987" y="846">5</text>
      <line x1="1060" y1="865" x2="1060" y2="901" stroke="var(--line)" stroke-width="1.5"/><circle cx="1060" cy="901" r="3.5" fill="var(--line)"/>
      <circle cx="1060" cy="815" r="50" fill="#fff" stroke="#8d8e91" stroke-width="2"/>
      <circle cx="1060" cy="815" r="42" fill="#fff" filter="url(#soft-shadow)"/>
      <path d="M1018 815 A42 42 0 0 0 1102 815 Z" fill="var(--blue-deep)"/>
      <text class="milestone-label" x="1060" y="831" text-anchor="middle">DONATIONS</text>
      <text class="milestone-label" x="1060" y="842" text-anchor="middle">AND CHARITY</text>
      <g class="icon"><path d="M1062 796 l-7 -7 a4 4 0 0 1 7 -4 a4 4 0 0 1 7 4 z M1048 806 l6 -4 h10 M1048 810 h18 l8 -6"/></g>
    </g>
  </g>
</svg>
</body>
</html>
```